Tarvel electrical letter head

Require a letter head to go with our new logo for our start up company. Something fresh and professional looking, also perhaps a "ghost"image of the logo in the centre of the page. Address to go on it PO Box 58, Orvendale 7563. Web address: www.tarvel.net.nz

```html
<!DOCTYPE html>
<html lang="en">
<head>
<meta charset="utf-8">
<title>Tarvel electrical – letterhead</title>
<link rel="stylesheet" href="https://fonts.googleapis.com/css2?family=Didact+Gothic&family=Roboto:wght@400&display=swap">
<style>
  :root {
    --backdrop: #e4e4e4;
    --paper: #f3f3f3;
    --paper-edge: #f7f7f7;
    --ink: #555555;
    --ink-soft: #6a6a6a;
    --brand-blue: #2f6db5;
    --brand-green: #a6cc2f;
    --rule: #8a8a8a;
  }
  * { box-sizing: border-box; margin: 0; padding: 0; }
  html, body {
    width: 1024px;
    height: 1200px;
    overflow: hidden;
    background: var(--backdrop);
  }
  .letterhead {
    position: absolute;
    left: 92px;
    top: 12px;
    width: 840px;
    height: 1176px;
    background: linear-gradient(100deg, var(--paper-edge) 0%, var(--paper) 60%, #ececec 100%);
    box-shadow: 0 4px 18px rgba(0,0,0,0.12);
    font-family: "Didact Gothic", "Century Gothic", sans-serif;
    color: var(--ink);
  }
  .brand {
    position: absolute;
    top: 84px;
    left: 0;
    width: 100%;
    display: flex;
    justify-content: center;
    align-items: center;
    gap: 10px;
  }
  .brand-dot {
    width: 22px;
    height: 22px;
    border-radius: 50%;
    background: var(--brand-green);
  }
  .brand-name {
    font-size: 34px;
    color: var(--brand-blue);
    letter-spacing: 0.5px;
  }
  .letter {
    position: absolute;
    left: 76px;
    top: 300px;
    width: 694px;
  }
  .salutation {
    font-size: 20px;
    font-weight: 400;
    color: var(--ink);
    margin-bottom: 40px;
  }
  .body-copy {
    font-size: 12.4px;
    line-height: 17px;
    color: var(--ink-soft);
    text-align: justify;
    margin-bottom: 17px;
  }
  .closing {
    font-size: 12.4px;
    color: var(--ink-soft);
    margin-top: 40px;
  }
  .signature {
    margin-top: 42px;
    width: 150px;
    height: 66px;
    border-radius: 6px;
    background: linear-gradient(90deg, rgba(47,109,181,0.18), rgba(47,109,181,0.08));
  }
  .footer {
    position: absolute;
    left: 0;
    width: 100%;
    top: 1088px;
    text-align: center;
    font-family: "Roboto", Arial, sans-serif;
    color: var(--ink-soft);
    font-size: 13.5px;
  }
  .footer-address {
    display: inline-block;
    padding: 0 6px 6px;
    border-bottom: 1px solid var(--rule);
  }
  .footer-services {
    margin-top: 7px;
    letter-spacing: 0.6px;
  }
</style>
</head>
<body>
  <main class="letterhead">
    <header class="brand">
      <span class="brand-dot"></span>
      <span class="brand-name">Tarvel electrical</span>
    </header>

    <section class="letter">
      <h1 class="salutation">Dear Mr. Hartley,</h1>
      <p class="body-copy">Lorem ipsum dolor sit amet, consectetur adipiscing elit. Donec orci purus, luctus vitae dignissim eu, iaculis sed purus. Vivamus faucibus, ipsum nec aliquet viverra, leo mauris condimentum ligula, sit amet sagittis enim ligula quis arcu. Nam egestas tortor id nisi porttitor mattis. In tortor ante, ultricies in suscipit a, tempus non massa. Vivamus et auctor mi. Fusce vel massa nulla. Phasellus nec eros mauris, et scelerisque orci.</p>
      <p class="body-copy">Donec malesuada orci vitae nulla accumsan porta a id massa. Quisque accumsan iaculis magna sit amet fringilla. Maecenas consequat, magna eget tincidunt semper, odio nibh rutrum mi, id feugiat ante nisi eu risus. Vestibulum nunc orci, rhoncus a placerat in, ultricies in mi. Cras mattis varius eros, vel fringilla nisi suscipit eget. Quisque scelerisque sagittis nulla at porttitor.</p>
      <p class="body-copy">Sed id augue vitae urna euismod commodo aliquet a quam. Pellentesque arcu velit, cursus et malesuada ut, consequat et diam. Nullam erat sem, rhoncus id ullamcorper vitae, rhoncus et arcu. In ultricies ultricies nulla, ut rutrum nisi iaculis at. Donec eu magna a metus ornare faucibus. Fusce aliquet faucibus ultricies. Morbi semper, est id tincidunt gravida, sem arcu adipiscing lacus, ac bibendum nulla leo eu purus. Quisque nec diam sed risus consectetur a ccumsan quis quis nibh. Vestibulum id purus lorem.</p>
      <p class="body-copy">It is a long established fact that a reader will be distracted by the readable content of a page when looking at its layout. The point of using Lorem Ipsum is that it has a more-or-less normal distribution of letters, as opposed to using 'Content here, content here', making it look like readable English. Many desktop publishing packages</p>
      <p class="closing">Sincerely,</p>
      <div class="signature" role="img" aria-label="Handwritten signature of Owen Hartley in blue ink"></div>
    </section>

    <footer class="footer">
      <div class="footer-address">PO Box 58, Orvendale 7563| www.tarvel.net.nz</div>
      <div class="footer-services">DESIGN &nbsp;|&nbsp; INSTALLATION &nbsp;|&nbsp; MAINTENANCE</div>
    </footer>
  </main>
</body>
</html>
```